New Business Card Design Project

I would like a business card to match my truck wrap and logo. I would like the font to match my existing business card please.

Industry/Entity Type

Painter

Contact Information for Business Card

Rodrigo Venter 801-437-2910 Ventercoatings.utah@brushmail.net
SERVICES - Custom Paint & Stain, Interior & Exterior, Epoxy Coatings / Garage Floors, Cabinet Refinishing, Log Staining and Refinishing.

Requirements
Nice to have
• I would like to have the white and grey line like the bottom of my vehicle wrap, Light Grey to match my truck also.

```html
<!DOCTYPE html>
<html lang="en">
<head>
<meta charset="utf-8">
<title>Venter Coatings – Business Card</title>
<link rel="stylesheet" href="https://fonts.googleapis.com/css2?family=Arimo:wght@400;700&display=swap">
<style>
  :root {
    --backdrop: #666666;
    --card-white: #ffffff;
    --band-grey: #aaaeb8;
    --brand-blue: #0fa6e4;
    --deep-blue: #0b74bb;
    --back-top: #02aeee;
    --back-bottom: #0f5a98;
    --text-grey: #ffffff;
  }
  * { margin: 0; padding: 0; box-sizing: border-box; }
  html, body {
    width: 1200px; height: 801px; overflow: hidden;
    background: var(--backdrop);
    font-family: "Arimo", Arial, sans-serif;
  }
  .card {
    position: absolute; top: 274px;
    width: 443px; height: 263px; overflow: hidden;
  }
  .card-front { left: 153px; background: var(--card-white); }
  .card-back {
    left: 625px;
    background: linear-gradient(180deg, var(--back-top) 0%, #0a86c8 55%, var(--back-bottom) 100%);
  }
  .brand {
    position: absolute; left: 31px; top: 100px;
    display: flex; align-items: center; gap: 10px;
  }
  .brand-square {
    width: 22px; height: 22px; background: var(--brand-blue);
  }
  .brand-name {
    font-weight: 700; font-size: 25px; letter-spacing: 1px;
    color: var(--brand-blue); text-transform: uppercase;
  }
  .band { position: absolute; left: 0; top: 0; }
  .holder-name {
    position: absolute; left: 24px; top: 210px;
    font-weight: 700; font-size: 16px; letter-spacing: 0.3px;
    color: var(--deep-blue); text-transform: uppercase;
  }
  .contact {
    position: absolute; left: 219px; top: 205px;
    list-style: none; color: var(--text-grey);
    font-size: 12.5px; line-height: 16px;
  }
  .contact li { display: flex; align-items: center; gap: 6px; }
  .contact svg { width: 12px; height: 12px; flex: none; }
  .services {
    position: absolute; left: 95px; top: 66px;
    list-style: none; color: #ffffff; font-size: 15px;
  }
  .services li {
    display: flex; align-items: center; gap: 5px;
    height: 27.6px; text-transform: uppercase;
  }
  .services li::before {
    content: ""; width: 8px; height: 8px; border-radius: 50%;
    background: #ffffff; flex: none;
  }
</style>
</head>
<body>
  <section class="card card-front">
    <div class="brand">
      <span class="brand-square"></span>
      <span class="brand-name">Venter Coatings</span>
    </div>

    <svg class="band" width="443" height="263" viewBox="0 0 443 263">
      <polygon points="0,184 210,184 236,155 443,155 443,263 0,263" fill="var(--band-grey)"/>
      <polyline points="0,176 208,176 235,148 443,148" fill="none" stroke="var(--band-grey)" stroke-width="4"/>
    </svg>

    <p class="holder-name">Rodrigo Venter</p>

    <ul class="contact">
      <li>
        <svg viewBox="0 0 24 24"><path fill="var(--deep-blue)" d="M6.6 10.8a15.1 15.1 0 0 0 6.6 6.6l2.2-2.2a1 1 0 0 1 1-.25 11.4 11.4 0 0 0 3.6.57 1 1 0 0 1 1 1V20a1 1 0 0 1-1 1A17 17 0 0 1 3 4a1 1 0 0 1 1-1h3.5a1 1 0 0 1 1 1c0 1.25.2 2.45.57 3.57a1 1 0 0 1-.25 1z"/></svg>
        801-437-2910
      </li>
      <li>
        <svg viewBox="0 0 24 24"><rect x="2" y="5" width="20" height="14" fill="var(--deep-blue)"/><polyline points="2,5 12,13 22,5" fill="none" stroke="#ffffff" stroke-width="1.6"/></svg>
        Ventercoatings.utah@brushmail.net
      </li>
    </ul>
  </section>

  <section class="card card-back">
    <ul class="services">
      <li>Custom Paint &amp; Stain</li>
      <li>Interior &amp; Exterior</li>
      <li>Epoxy Coatings / Garage Floors</li>
      <li>Cabinet Refinishing</li>
      <li>Log Staining and Refinishing.</li>
    </ul>
  </section>
</body>
</html>
```